Copper & Wren Labels*

Hello :) I am needing labels for my herbal tea/petal product. I am a small producer for the local restaurants (edible flowers/micro herbs & dried product). I am hoping to sell the dried product online. It will be sold in batches as it is ready so quite small/boutique and the label needs to be somewhat generic for the range of produce I make.
Feels: no/minimal plastic, product is in a reusable mason jar, we use organic/regenerative principles from soil health to end product. Treading gently on the land. High quality i.e only fresh hand picked leaf tips for the tea.

```html
<!DOCTYPE html>
<html lang="en">
<head>
<meta charset="utf-8">
<title>Copper &amp; Wren – Labels</title>
<link rel="stylesheet" href="https://fonts.googleapis.com/css2?family=Special+Elite&family=Courier+Prime&family=Lobster&family=Delius&family=Oswald:wght@500&family=Montserrat:wght@600&display=swap">
<style>
  :root {
    --bg-top: #e3e3e3;
    --bg-bottom: #f4f4f4;
    --paper: #eeeeec;
    --ink: #1f1f1f;
    --board: #1b1b1b;
    --chalk: #f6f6f2;
    --leaf-green: #2f8a3c;
    --brand-green: #2e9b3a;
    --rule: #b9b9b6;
    --flower: #d9cde0;
    --flag: #1f3f8f;
  }
  * { margin: 0; padding: 0; box-sizing: border-box; }
  html, body { width: 1200px; height: 875px; overflow: hidden; }
  body {
    background: linear-gradient(180deg, var(--bg-top), var(--bg-bottom));
    position: relative;
    color: var(--ink);
  }

  /* ---------- front label ---------- */
  .front-label {
    position: absolute;
    left: 323px; top: 377px;
    width: 215px; height: 330px;
    background: var(--paper);
    box-shadow: 0 1px 3px rgba(0,0,0,.12);
  }
  .brand {
    position: absolute; left: 0; right: 0; top: 13px;
    display: flex; flex-direction: column; align-items: center;
  }
  .brand-dot {
    width: 52px; height: 52px; border-radius: 50%;
    background: var(--brand-green);
  }
  .brand-name {
    margin-top: 8px;
    font-family: "Montserrat", sans-serif; font-weight: 600;
    font-size: 15px; color: var(--ink); letter-spacing: .2px;
  }
  .title-board {
    position: absolute; left: 21px; top: 90px;
    width: 173px; height: 140px;
  }
  .title-board svg { position: absolute; inset: 0; }
  .title-text {
    position: absolute; inset: 0;
    display: flex; flex-direction: column; align-items: center; justify-content: center;
    font-family: "Special Elite", monospace; color: var(--chalk);
    line-height: .95; padding-left: 8px;
  }
  .title-word { font-size: 40px; letter-spacing: 1px; }
  .title-amp { font-size: 22px; margin: 2px 0; }
  .flower-art {
    position: absolute; left: 8px; top: 185px;
    width: 60px; height: 58px; border-radius: 50%;
    background: radial-gradient(circle at 45% 45%, #9a4d8e 0 14%, var(--flower) 40%, #f3f0f3 75%);
  }
  .claim {
    position: absolute; left: 0; right: 0; top: 252px;
    text-align: center;
    font-family: "Oswald", sans-serif; font-weight: 500;
    font-size: 14px; color: var(--leaf-green); letter-spacing: .3px;
  }
  .origin-line {
    position: absolute; left: 20px; right: 10px; top: 283px;
    font-family: "Delius", cursive; font-size: 12.5px; line-height: 1.45;
    text-align: center; transform: rotate(-2deg);
  }

  /* ---------- back label ---------- */
  .back-label {
    position: absolute;
    left: 715px; top: 489px;
    width: 187px; height: 208px;
    background: var(--paper);
    box-shadow: 0 1px 3px rgba(0,0,0,.12);
  }
  .spec-table {
    position: absolute; left: 15px; top: 21px;
    width: 157px; height: 160px;
    border: 1px solid var(--rule);
    border-collapse: collapse;
    font-family: "Courier Prime", monospace; font-size: 8px;
  }
  .spec-table th {
    font-family: "Lobster", cursive; font-weight: 400;
    font-size: 12.5px; text-align: left;
    padding: 5px 6px 3px; height: 27px;
    border-bottom: 1px solid var(--rule);
  }
  .spec-table td {
    vertical-align: top; padding: 4px 6px;
    border-bottom: 1px solid var(--rule);
  }
  .spec-table td + td { border-left: 1px solid var(--rule); }
  .row-leaf td { height: 39px; line-height: 1.25; }
  .row-petals td, .row-batch td { height: 26px; }
  .row-origin td { height: 42px; vertical-align: middle; border-bottom: 0; }
  .origin-cell { display: flex; align-items: center; justify-content: space-between; line-height: 1.25; }
  .flag {
    width: 34px; height: 21px; background: var(--flag); margin-right: 14px;
  }
</style>
</head>
<body>

<section class="front-label">
  <div class="brand">
    <div class="brand-dot"></div>
    <div class="brand-name">fernhollow</div>
  </div>

  <div class="title-board">
    <svg viewBox="0 0 173 140" width="173" height="140" aria-hidden="true">
      <path d="M4 6 L168 2 L171 134 L6 138 Z" fill="none" stroke="var(--leaf-green)" stroke-width="1.6"/>
      <path d="M9 10 L164 7 L166 130 L11 133 Z" fill="var(--board)"/>
    </svg>
    <div class="title-text">
      <span class="title-word">COPPER</span>
      <span class="title-amp">&amp;</span>
      <span class="title-word">WREN</span>
    </div>
  </div>

  <div class="flower-art" role="img" aria-label="Illustration of three pink and white cornflower blossoms"></div>

  <p class="claim">CHEMICAL FREE</p>
  <p class="origin-line">Grown, harvested and dried on our farm in east Gippsland</p>
</section>

<section class="back-label">
  <table class="spec-table">
    <tr><th colspan="2">Single Origin Herbal Tee</th></tr>
    <tr class="row-leaf"><td>Leaf base</td><td>Lemon<br>Verbena<br>Agastache</td></tr>
    <tr class="row-petals"><td>Petals</td><td></td></tr>
    <tr class="row-batch"><td>Batch</td><td></td></tr>
    <tr class="row-origin">
      <td colspan="2">
        <div class="origin-cell">
          <span>Tallow Creek<br>Victoria Australia</span>
          <div class="flag" role="img" aria-label="Australian flag"></div>
        </div>
      </td>
    </tr>
  </table>
</section>

</body>
</html>
```